Business Card Design Project

Personal Service. There are three areas of my service: Resourceful/Recycling Consultation, Life Coaching using Law of Attraction & Visualization Board. My current cards has: Clearview to Creation. I would like to work with this theme

Industry/Entity Type

Business

Contact Information for Business Card

Circles. Recyling Triangle

```html
<!DOCTYPE html>
<html lang="en">
<head>
<meta charset="utf-8">
<title>Clearview to Creation – Business Card</title>
<link rel="stylesheet" href="https://fonts.googleapis.com/css2?family=Cinzel:wght@400&family=PT+Sans:wght@400;700&display=swap">
<style>
  :root {
    --stage: #3a3a3a;
    --card-light: #ececec;
    --magenta: #b5106a;
    --magenta-deep: #b80a68;
    --magenta-bright: #e8449f;
    --leaf-green: #7cbb3a;
    --ink: #3c3c3c;
    --rule: #8a8a8a;
    --white: #ffffff;
  }
  * { margin: 0; padding: 0; box-sizing: border-box; }
  html, body {
    width: 1200px; height: 900px; overflow: hidden;
    background: var(--stage);
  }
  .canvas { position: relative; width: 1200px; height: 900px; }

  .card {
    position: absolute; top: 170px;
    width: 347px; height: 560px;
    text-align: center;
  }
  .card--front { left: 259px; background: var(--card-light); }
  .card--back {
    left: 631px;
    background: linear-gradient(115deg,
      var(--magenta-bright) 0%, #c8157a 28%, var(--magenta-deep) 48%,
      #bf0f6d 76%, var(--magenta-bright) 93%, #e44199 100%);
  }

  .brand-mark {
    position: absolute; left: 0; right: 0;
    font-family: "Cinzel", serif; font-weight: 400;
    line-height: 1.15;
  }
  .card--front .brand-mark { top: 110px; color: var(--magenta); font-size: 27px; }
  .card--back .brand-mark { top: 130px; color: var(--white); font-size: 31px; }
  .brand-mark__dot {
    display: block; width: 18px; height: 18px; border-radius: 50%;
    margin: 0 auto 14px; background: currentColor;
  }

  .holder-name {
    position: absolute; top: 318px; left: 0; right: 0;
    font-family: "Cinzel", serif; font-size: 25px; letter-spacing: 0.5px;
    color: var(--magenta);
  }
  .holder-name__last { color: var(--leaf-green); }
  .holder-title {
    position: absolute; top: 348px; left: 0; right: 0;
    font-family: "PT Sans", sans-serif; font-size: 16px; color: var(--ink);
  }
  .divider {
    position: absolute; left: 93px; width: 162px; height: 1px;
    background: var(--rule);
  }
  .divider--top { top: 380px; }
  .divider--bottom { top: 470px; }

  .contact-list {
    position: absolute; top: 394px; left: 0; right: 0;
    list-style: none;
    font-family: "PT Sans", sans-serif; font-size: 15.5px; line-height: 20px;
    color: var(--ink);
  }
  .contact-list__label { color: var(--magenta); font-weight: 700; }

  .address {
    position: absolute; top: 483px; left: 0; right: 0;
    font-family: "PT Sans", sans-serif; font-size: 15.5px; line-height: 21px;
    font-style: normal; color: var(--ink);
  }

  .service-list {
    position: absolute; top: 452px; left: 0; right: 0;
    list-style: none;
    font-family: "PT Sans", sans-serif; font-size: 15.5px; line-height: 20px;
    color: var(--white);
  }
</style>
</head>
<body>
<main class="canvas">
  <section class="card card--front" aria-label="Card front">
    <div class="brand-mark"><span class="brand-mark__dot"></span>Clearview<br>to Creation</div>
    <h1 class="holder-name">Daniel <span class="holder-name__last">Hart</span></h1>
    <p class="holder-title">Managing Director</p>
    <div class="divider divider--top"></div>
    <ul class="contact-list">
      <li><span class="contact-list__label">P:</span> 055-210 348 617</li>
      <li><span class="contact-list__label">M:</span> 055-210 348 672</li>
      <li><span class="contact-list__label">E:</span> hello@clearview.co</li>
    </ul>
    <div class="divider divider--bottom"></div>
    <address class="address">48 Willow Lane, Suite 12<br>Northland, 204518.</address>
  </section>

  <section class="card card--back" aria-label="Card back">
    <div class="brand-mark"><span class="brand-mark__dot"></span>Clearview<br>to Creation</div>
    <ul class="service-list">
      <li>Resourceful/Recycling Consultation</li>
      <li>Life Coaching using Law of Attraction</li>
      <li>Visualization Board</li>
    </ul>
  </section>
</main>
</body>
</html>
```